Thumbnail for "Exclusive Shows"

I need a Thumbnail / Cover for exclusive shows I'll upload to loopmarsh. It should be unique and especially made for this purpose. My channel delivers electronic dance music and thus should be seen in the thumbnail / cover. There will be now attached files so there is nothing to influence you in your work.

Target Market(s)

Young people enjoying electronic dance music

Colors
e667a6
876aae
f04a50
f68d4d
33a6d7
3176b5

Requirements
Must have
• The design should include my logo (which will be the only thing provided later this day).
Nice to have
• Would it be good to keep it simple with texting. If you want to integrate the word "Exclusive" or "Exclusive Show" it will fit as long as it's fit to the whole design.

```html
<!DOCTYPE html>
<html lang="en">
<head>
<meta charset="utf-8">
<title>Tempovera – Exclusive Show</title>
<link rel="stylesheet" href="https://fonts.googleapis.com/css2?family=Nunito:wght@900&family=Questrial&display=swap">
<style>
  :root {
    --navy-deep: #071a4a;
    --navy: #0d2a6e;
    --blue-glow: #33a6d7;
    --blue-mid: #3176b5;
    --orange: #f68d4d;
    --red-orange: #f04a50;
    --cream: #f3ecd9;
    --white-pink: #fdf2f4;
    --outline-dark: #0a1633;
  }
  * { margin: 0; padding: 0; box-sizing: border-box; }
  html, body { width: 1200px; height: 1200px; overflow: hidden; background: var(--navy-deep); }
  .cover { position: relative; width: 1200px; height: 1200px; overflow: hidden; }
  .backdrop {
    position: absolute; inset: 0;
    background:
      radial-gradient(circle at 78% 62%, rgba(240,74,80,0.45) 0%, rgba(246,141,77,0.15) 22%, transparent 40%),
      radial-gradient(circle at 50% 50%, #1c4fa8 0%, #12367f 40%, var(--navy-deep) 85%);
  }
  .rings { position: absolute; inset: 0; }
  .brand-band {
    position: absolute; left: 292px; width: 616px; height: 8px;
    background: var(--blue-glow);
  }
  .brand-band.top { top: 363px; }
  .brand-band.bottom { top: 460px; }
  .brand-name {
    position: absolute; left: 292px; width: 616px; top: 380px;
    text-align: center;
    font-family: "Nunito", sans-serif; font-weight: 900;
    font-size: 72px; line-height: 76px; letter-spacing: 6px;
    color: var(--blue-glow);
  }
  .headline { position: absolute; left: 0; top: 480px; width: 1200px; height: 320px; }
  .headline text {
    font-family: "Nunito", sans-serif; font-weight: 900;
    font-size: 158px; text-anchor: middle; letter-spacing: -2px;
    stroke-linejoin: round;
  }
  .socials {
    position: absolute; left: 0; width: 1200px; top: 1046px;
    display: flex; justify-content: center; align-items: center; gap: 16px;
    font-family: "Questrial", sans-serif; font-size: 21px; color: var(--cream);
    letter-spacing: 0.5px;
  }
  .social-item { display: flex; align-items: center; gap: 14px; }
  .social-dot {
    width: 34px; height: 34px; border-radius: 50%; background: var(--cream); flex: none;
  }
  .site-url {
    position: absolute; left: 0; width: 1200px; top: 1088px; text-align: center;
    font-family: "Questrial", sans-serif; font-size: 19px; color: var(--cream); letter-spacing: 1px;
  }
</style>
</head>
<body>
<div class="cover">
  <div class="backdrop" role="img" aria-label="Glowing blue geometric sci-fi stage with neon triangles and orange light rays"></div>

  <svg class="rings" width="1200" height="1200" viewBox="0 0 1200 1200" aria-hidden="true">
    <defs>
      <filter id="glow" x="-20%" y="-20%" width="140%" height="140%">
        <feGaussianBlur stdDeviation="6" result="b"/>
        <feMerge><feMergeNode in="b"/><feMergeNode in="SourceGraphic"/></feMerge>
      </filter>
    </defs>
    <circle cx="600" cy="600" r="547" fill="none" stroke="#6fd0ff" stroke-width="4" filter="url(#glow)" opacity="0.85"/>
    <circle cx="612" cy="620" r="430" fill="none" stroke="#f68d4d" stroke-width="4" filter="url(#glow)" opacity="0.75"/>
    <path d="M 960 360 A 430 430 0 0 1 940 900" fill="none" stroke="#f04a50" stroke-width="14" filter="url(#glow)" opacity="0.6"/>
  </svg>

  <div class="brand-band top"></div>
  <div class="brand-name">TEMPOVERA</div>
  <div class="brand-band bottom"></div>

  <svg class="headline" width="1200" height="320" viewBox="0 0 1200 320" role="img" aria-label="Exclusive Show">
    <g aria-hidden="true">
      <text x="600" y="140" fill="none" stroke="#f3ecd9" stroke-width="40" opacity="0.35">EXCLUSIVE</text>
      <text x="600" y="140" fill="none" stroke="#0a1633" stroke-width="32">EXCLUSIVE</text>
      <text x="600" y="140" fill="none" stroke="#f3ecd9" stroke-width="25">EXCLUSIVE</text>
      <text x="600" y="140" fill="none" stroke="#0a1633" stroke-width="19">EXCLUSIVE</text>
      <text x="600" y="140" fill="none" stroke="#f3ecd9" stroke-width="13">EXCLUSIVE</text>
      <text x="600" y="140" fill="none" stroke="#0a1633" stroke-width="6">EXCLUSIVE</text>
      <text x="600" y="275" fill="none" stroke="#f3ecd9" stroke-width="40" opacity="0.35">SHOW</text>
      <text x="600" y="275" fill="none" stroke="#0a1633" stroke-width="32">SHOW</text>
      <text x="600" y="275" fill="none" stroke="#f3ecd9" stroke-width="25">SHOW</text>
      <text x="600" y="275" fill="none" stroke="#0a1633" stroke-width="19">SHOW</text>
      <text x="600" y="275" fill="none" stroke="#f3ecd9" stroke-width="13">SHOW</text>
      <text x="600" y="275" fill="none" stroke="#0a1633" stroke-width="6">SHOW</text>
    </g>
    <text x="600" y="140" fill="#fdf2f4">EXCLUSIVE</text>
    <text x="600" y="275" fill="#fdf2f4">SHOW</text>
  </svg>

  <div class="socials">
    <span class="social-item"><span class="social-dot"></span>/Tempovera&nbsp;&nbsp;DJ</span>
    <span class="social-item"><span class="social-dot"></span>@tempovera&nbsp;&nbsp;DJ</span>
    <span class="social-item"><span class="social-dot"></span>loopmarsh&nbsp;&nbsp;/tempovera&nbsp;&nbsp;DJ</span>
    <span class="social-item"><span class="social-dot"></span>/tempo_vera</span>
  </div>
  <div class="site-url">www.tempo-vera.com</div>
</div>
</body>
</html>
```